Tolvey Arts and Entertainment

We need a web design for a new weekly online publication to be launched in Marin County, California...an upscale audience of sophisticated readers
who appreciate the arts: Sections will include music, art, books, theatre, dance, community events, kids events and a section named "Late Lantern", which is basically a restaurant section..where to go after a performance to get a bite.. Under each section there will be a listing of events, a profile of a performer, a review and a sponsored ad. Letters to the editor will make this publication interactive The site will include video and photos,
Updates

Reason: I suspect that a website design will take more time than allotted above. Hence, the extension to the 24th. Thank you! Rosalind Pettak

Industry/Entity Type

Entertainment

```html
<!DOCTYPE html>
<html lang="en">
<head>
<meta charset="utf-8">
<title>Tolvey Arts &amp; Entertainment</title>
<link href="https://fonts.googleapis.com/css2?family=Open+Sans:wght@400;600;700&family=Questrial&display=swap" rel="stylesheet">
<style>
:root{
  --red:#f25a45;
  --red-dark:#d9432f;
  --red-deep:#c93a28;
  --ink:#2b2b2b;
  --text:#555;
  --muted:#999;
  --line:#e6e6e6;
  --panel:#f2f2f2;
  --white:#fff;
  --star:#f2b824;
}
*{box-sizing:border-box;margin:0;padding:0}
html,body{width:686px;height:1200px;overflow:hidden;background:var(--white)}
body{position:relative;font-family:"Open Sans",Arial,sans-serif;color:var(--text)}
a{color:inherit;text-decoration:none}

/* header */
.brand{position:absolute;left:57px;top:22px}
.brand-name{font-family:"Questrial",Arial,sans-serif;font-size:21px;color:var(--red);letter-spacing:.5px;line-height:1}
.brand-tag{font-size:9.5px;color:#555;letter-spacing:.4px;margin-top:5px}
.search{position:absolute;left:460px;top:19px;width:169px;height:20px;border:1px solid #ddd;display:flex}
.search span{flex:1;font-size:7px;color:#666;padding:6px 6px}
.search i{width:20px;background:var(--red);display:flex;align-items:center;justify-content:center}
.account{position:absolute;right:57px;top:50px;display:flex;gap:2px}
.account a{font-size:6.5px;color:#fff;padding:2px 4px;background:var(--red)}
.account a.login{background:#8a8a8a}

/* nav */
.main-nav{position:absolute;left:0;top:80px;width:686px;height:25px;background:var(--red);border-top:2px solid var(--red-dark)}
.main-nav ul{list-style:none;display:flex;margin-left:58px;height:100%}
.main-nav li{font-size:8px;color:#fff;padding:0 12.4px;display:flex;align-items:center}
.main-nav li.active{background:var(--red-deep);padding:0 11px}

/* hero */
.hero{position:absolute;left:57px;top:123px;width:571px;height:260px;background:linear-gradient(120deg,#c9a543 0%,#e8c763 35%,#f6dc7a 55%,#c59b3a 80%,#a8852f 100%)}
.hero-shadow{position:absolute;left:90px;top:383px;width:505px;height:14px;background:radial-gradient(ellipse at top,rgba(0,0,0,.18),transparent 70%)}
.hero-arrow{position:absolute;top:120px;width:17px;height:17px;border-radius:50%;background:#fff;display:flex;align-items:center;justify-content:center}
.hero-arrow.prev{left:17px}.hero-arrow.next{right:17px}
.hero-title{position:absolute;left:51px;top:104px;font-family:"Questrial",Arial,sans-serif;color:#fff;font-size:28px;line-height:1}
.hero-title span{display:inline-block;background:rgba(242,90,69,.85);padding:3px 4px 2px;margin-bottom:3px}
.hero-copy{position:absolute;left:51px;top:174px;font-family:"Questrial",Arial,sans-serif;color:#fff;font-size:10px;line-height:13px}
.hero-copy span{background:rgba(40,40,40,.8);padding:0 2px}

/* sections */
.section-title{position:absolute;font-size:15px;color:var(--ink);font-weight:400}
.events{position:absolute;left:57px;top:443px;width:378px}
.card{position:absolute;border:1px solid #eee;background:#fff}
.card-img{display:block;width:100%}
.card-body{padding:5px 7px}
.card h3{font-size:7.4px;font-weight:400;color:#444;line-height:10px}
.meta{font-size:5.6px;color:var(--muted);margin-top:3px}
.meta em{font-style:normal;color:var(--red)}
.stars{font-size:6px;letter-spacing:-.5px;color:#ddd;line-height:8px}
.stars b{color:var(--star);font-weight:400}
.card p{font-size:5.6px;line-height:9px;color:#666;margin-top:6px}
.card p em{color:var(--red)}
.load-more{position:absolute;left:212px;top:931px;width:71px;height:16px;background:var(--red);color:#fff;font-size:8px;text-align:center;line-height:16px}

/* reviews */
.review-nav{position:absolute;left:420px;top:986px;font-size:13px;color:var(--red)}
.review{position:absolute;top:1020px;width:190px;height:56px}
.review-photo{position:absolute;left:0;top:0;width:62px;height:52px}
.review-quote{position:absolute;left:72px;top:0;font-size:22px;color:#ccc;font-family:Georgia,serif;line-height:1}
.review-text{position:absolute;left:72px;top:6px;width:118px;font-family:Georgia,serif;font-size:6px;line-height:9.2px;color:#333;text-align:justify;text-indent:22px}
.review-name{position:absolute;left:72px;top:41px;font-family:Georgia,serif;font-size:7px;color:#222}
.review-role{position:absolute;left:72px;top:51px;font-size:5px;color:#999}
.review-role em{font-style:normal;color:#3a7bd5}

/* sidebar */
.profile{position:absolute;left:468px;top:438px;width:161px;height:174px;background:#fff;box-shadow:0 1px 3px rgba(0,0,0,.18);text-align:center}
.profile-photo{position:absolute;left:30px;top:12px;width:102px;height:68px}
.profile .chev{position:absolute;top:34px;font-size:12px;color:#aaa}
.profile-name{position:absolute;top:87px;width:100%;font-size:10.5px;color:#222}
.profile-role{position:absolute;top:103px;width:100%;font-size:7px;font-weight:700;color:#222}
.profile-social{position:absolute;top:119px;left:0;width:100%;display:flex;justify-content:center;gap:14px}
.profile-btn{position:absolute;left:40px;top:141px;width:76px;height:14px;border-radius:7px;background:var(--red);color:#fff;font-size:7.5px;line-height:14px}
.ads{position:absolute;left:466px;top:624px;width:161px;height:402px;background:var(--panel);border:1px solid #e4e4e4}
.ad{position:absolute;width:67px;height:67px}
.ads-link{position:absolute;top:386px;width:100%;text-align:center;font-size:8px;color:#3a7bd5}

/* footer */
.site-footer{position:absolute;left:0;top:1143px;width:686px;height:57px;background:linear-gradient(#f25a45,#f47c52)}
.footer-nav{display:flex;justify-content:center;margin-top:14px;font-size:6.5px;color:#fff;margin-left:-10px}
.footer-nav span{padding:0 7px}
.footer-nav i{font-style:normal}
.copyright{position:absolute;left:57px;top:40px;font-size:6.5px;color:#fff}
.footer-social{position:absolute;left:580px;top:37px;display:flex;gap:6px}
.footer-social span{width:11px;height:11px;border-radius:50%;background:#fff;display:block}
</style>
</head>
<body>

<header>
  <div class="brand">
    <div class="brand-name">TOLVEY</div>
    <div class="brand-tag">ARTS &amp; ENTERTAINMENT</div>
  </div>
  <div class="search"><span>Search</span><i><svg width="9" height="9" viewBox="0 0 10 10"><circle cx="6" cy="4" r="3" fill="none" stroke="#fff" stroke-width="1.2"/><line x1="4" y1="6" x2="1" y2="9" stroke="#fff" stroke-width="1.2"/></svg></i></div>
  <div class="account"><a href="#">Join us</a><a href="#" class="login">Login</a></div>
</header>

<nav class="main-nav">
  <ul>
    <li class="active">Home</li><li>Music</li><li>Art</li><li>Books</li><li>Theatre</li><li>Dance</li><li>Community Events</li><li>Kids Events</li><li>Late Lantern</li><li>Contact Us</li>
  </ul>
</nav>

<section class="hero" role="img" aria-label="Photo of a parent lying in sunlit grass lifting a laughing child, with trees behind">
  <span class="hero-arrow prev"><svg width="8" height="8" viewBox="0 0 8 8"><path d="M5 1L2 4l3 3" fill="none" stroke="#444" stroke-width="1.4"/></svg></span>
  <span class="hero-arrow next"><svg width="8" height="8" viewBox="0 0 8 8"><path d="M3 1l3 3-3 3" fill="none" stroke="#444" stroke-width="1.4"/></svg></span>
  <h1 class="hero-title"><span>LOREM IPS</span><br><span>CONTANTRY POPI</span></h1>
  <p class="hero-copy"><span>Lorem ipsum dolor sit amet, co</span><br><span>nsectetur adipiscing elit. Ut in ult</span><br><span>rices libero. Integer condimentum tincidunt ex,</span></p>
</section>
<div class="hero-shadow"></div>

<h2 class="section-title" style="left:57px;top:417px">Events listings</h2>

<section class="events">
  <article class="card" style="left:0;top:0;width:187px;height:122px">
    <svg class="card-img" width="185" height="81" role="img" aria-label="Close-up of a paintbrush on a textured canvas"><rect width="185" height="81" fill="#8fa3b8"/><rect width="185" height="81" fill="url(#g1)"/><defs><linearGradient id="g1"><stop offset="0" stop-color="#6e7f93"/><stop offset=".5" stop-color="#b9c6d2"/><stop offset="1" stop-color="#d6a27a"/></linearGradient></defs></svg>
    <div class="card-body"><h3>Quisque faucibus, ante eget molestie luctus, orci</h3><div class="meta">Posted on <em>7 April, 2013</em> By <em>Lorem</em></div><div class="stars"><b>★★</b>★★★</div></div>
  </article>
  <article class="card" style="left:191px;top:0;width:187px;height:122px">
    <svg class="card-img" width="185" height="81" role="img" aria-label="Hanging light bulbs against a teal wall"><defs><linearGradient id="g2" x1="0" y1="0" x2="1" y2="1"><stop offset="0" stop-color="#3f7f82"/><stop offset="1" stop-color="#8fb8b3"/></linearGradient></defs><rect width="185" height="81" fill="url(#g2)"/></svg>
    <div class="card-body"><h3>Quisque faucibus, ante eget molestie luctus, orci</h3><div class="meta">Posted on <em>7 April, 2013</em> By <em>Lorem</em></div><div class="stars"><b>★★</b>★★★</div></div>
  </article>

  <article class="card" style="left:0;top:127px;width:123px;height:163px">
    <svg class="card-img" width="121" height="55" role="img" aria-label="Open book on a wooden shelf"><defs><linearGradient id="g3"><stop offset="0" stop-color="#c9a36a"/><stop offset="1" stop-color="#8a5a3a"/></linearGradient></defs><rect width="121" height="55" fill="url(#g3)"/></svg>
    <div class="card-body"><h3>Quisque faucibus, ante eget molestie luctus</h3><div class="meta">Posted on <em>7 April, 2013</em> By <em>Lorem</em></div><div class="stars"><b>★★</b>★★★</div><p>Dreaming of an overseas move can be so exciting that it is often hard to focus on the dreary matter of money – but some smart decisions and simple planning could save… <em>Continue Reading</em></p></div>
  </article>
  <article class="card" style="left:127px;top:127px;width:124px;height:163px">
    <svg class="card-img" width="122" height="55" role="img" aria-label="Two children in striped costume hats outdoors"><defs><linearGradient id="g4"><stop offset="0" stop-color="#a3602f"/><stop offset="1" stop-color="#6f8a3c"/></linearGradient></defs><rect width="122" height="55" fill="url(#g4)"/></svg>
    <div class="card-body"><h3>Quisque faucibus, ante eget molestie luctus, orci elit</h3><div class="meta">Posted on <em>7 April, 2013</em> By <em>Lorem</em></div><div class="stars"><b>★★</b>★★★</div><p>Dreaming of an overseas move can be so exciting that it is often hard to focus on the dreary matter of money – but some smart decisions and simple planning could save… <em>Continue Reading</em></p></div>
  </article>
  <article class="card" style="left:255px;top:127px;width:123px;height:163px">
    <svg class="card-img" width="121" height="55" role="img" aria-label="Paint palette with bright colours"><defs><linearGradient id="g5"><stop offset="0" stop-color="#d9a531"/><stop offset=".6" stop-color="#4f6fa8"/><stop offset="1" stop-color="#c84a3a"/></linearGradient></defs><rect width="121" height="55" fill="url(#g5)"/></svg>
    <div class="card-body"><h3>Quisque faucibus, ante eget molestie luctus, orci elit sodales</h3><div class="meta">Posted on <em>7 April, 2013</em> By <em>Lorem</em></div><div class="stars"><b>★★</b>★★★</div><p>Dreaming of an overseas move can be so exciting that it is often hard to focus on the dreary matter of money – but some smart decisions and simple planning could save… <em>Continue Reading</em></p></div>
  </article>

  <article class="card" style="left:0;top:305px;width:123px;height:163px">
    <svg class="card-img" width="121" height="55" role="img" aria-label="Child in aviator goggles against a cloudy sky"><defs><linearGradient id="g6"><stop offset="0" stop-color="#5f6a72"/><stop offset="1" stop-color="#9fa8a8"/></linearGradient></defs><rect width="121" height="55" fill="url(#g6)"/></svg>
    <div class="card-body"><h3>Quisque faucibus, ante eget molestie luctus</h3><div class="meta">Posted on <em>7 April, 2013</em> By <em>Lorem</em></div><div class="stars"><b>★★</b>★★★</div><p>Dreaming of an overseas move can be so exciting that it is often hard to focus on the dreary matter of money – but some smart decisions and simple planning could save… <em>Continue Reading</em></p></div>
  </article>
  <article class="card" style="left:127px;top:305px;width:124px;height:163px">
    <svg class="card-img" width="122" height="55" role="img" aria-label="Paintbrushes over a yellow-green watercolour wash"><defs><linearGradient id="g7"><stop offset="0" stop-color="#d7e07a"/><stop offset="1" stop-color="#a7c45a"/></linearGradient></defs><rect width="122" height="55" fill="url(#g7)"/></svg>
    <div class="card-body"><h3>Quisque faucibus, ante eget molestie luctus, orci elit</h3><div class="meta">Posted on <em>7 April, 2013</em> By <em>Lorem</em></div><div class="stars"><b>★★</b>★★★</div><p>Dreaming of an overseas move can be so exciting that it is often hard to focus on the dreary matter of money – but some smart decisions and simple planning could save… <em>Continue Reading</em></p></div>
  </article>
  <article class="card" style="left:255px;top:305px;width:123px;height:163px">
    <svg class="card-img" width="121" height="55" role="img" aria-label="Stack of books on a wooden table"><defs><linearGradient id="g8"><stop offset="0" stop-color="#e9ddcb"/><stop offset="1" stop-color="#b9a285"/></linearGradient></defs><rect width="121" height="55" fill="url(#g8)"/></svg>
    <div class="card-body"><h3>Quisque faucibus, ante eget molestie luctus, orci elit sodales</h3><div class="meta">Posted on <em>7 April, 2013</em> By <em>Lorem</em></div><div class="stars"><b>★★</b>★★★</div><p>Dreaming of an overseas move can be so exciting that it is often hard to focus on the dreary matter of money – but some smart decisions and simple planning could save… <em>Continue Reading</em></p></div>
  </article>
</section>

<a class="load-more" href="#">Load More</a>

<h2 class="section-title" style="left:56px;top:983px">User reviews</h2>
<div class="review-nav">‹›</div>

<article class="review" style="left:58px">
  <div class="review-photo" role="img" aria-label="Portrait of a smiling reviewer" style="background:linear-gradient(#7f8890,#c9cdd0)"></div>
  <div class="review-quote">“</div>
  <p class="review-text">Pellentesque et pulvinar enim. Quisque at tempor ligula. Donec ut purus sed tortor malesuada.</p>
  <div class="review-name">Corin Valdt</div>
  <div class="review-role">Art Director / <em>lorem ipsum</em></div>
</article>
<article class="review" style="left:258px">
  <div class="review-photo" role="img" aria-label="Portrait of a reviewer in glasses" style="background:linear-gradient(#5a5a5a,#9a9a9a)"></div>
  <div class="review-quote">“</div>
  <p class="review-text">Pellentesque et pulvinar enim. Quisque at tempor ligula. Donec ut purus sed tortor malesuada.</p>
  <div class="review-name">Corin Valdt</div>
  <div class="review-role">Art Director / <em>lorem ipsum</em></div>
</article>

<h2 class="section-title" style="left:466px;top:417px">Performers profile</h2>
<aside class="profile">
  <span class="chev" style="left:14px">‹</span><span class="chev" style="right:16px">›</span>
  <div class="profile-photo" role="img" aria-label="Black and white performer portrait" style="background:linear-gradient(#1c1c1c,#5a5a5a)"></div>
  <div class="profile-name">NAME SURNAME</div>
  <div class="profile-role">Lorem ipsum dolor</div>
  <div class="profile-social">
    <svg width="10" height="10"><rect x="1" y="1" width="8" height="8" fill="#666"/></svg>
    <svg width="10" height="10"><rect x="1" y="1" width="8" height="8" fill="#666"/></svg>
  </div>
  <a class="profile-btn" href="#">View Profile</a>
</aside>

<aside class="ads">
  <div class="ad" role="img" aria-label="Sponsor ad" style="left:9px;top:9px;background:#e8697a"></div>
  <div class="ad" role="img" aria-label="Sponsor ad" style="left:84px;top:9px;background:#36e02a"></div>
  <div class="ad" role="img" aria-label="Sponsor ad" style="left:9px;top:84px;background:#1d2630"></div>
  <div class="ad" role="img" aria-label="Sponsor ad" style="left:84px;top:84px;background:#2f6b34"></div>
  <div class="ad" role="img" aria-label="Sponsor ad with illustrated hills" style="left:9px;top:160px;background:linear-gradient(#f3d67a,#9bbb45)"></div>
  <div class="ad" role="img" aria-label="Sponsor ad" style="left:84px;top:160px;background:linear-gradient(#fff 0 70%,#f6a21e 70%)"></div>
  <div class="ad" role="img" aria-label="Sponsor ad with printed cards" style="left:9px;top:236px;background:linear-gradient(#d8d8d8,#8a8a8a)"></div>
  <div class="ad" role="img" aria-label="Sponsor ad with paint palette" style="left:84px;top:236px;background:linear-gradient(#eaeaea,#d7c08a)"></div>
  <div class="ad" role="img" aria-label="Sponsor ad" style="left:9px;top:311px;background:#2e2e2e"></div>
  <a class="ads-link" href="#">Advertise Here</a>
</aside>

<footer class="site-footer">
  <nav class="footer-nav">
    <span>Home</span><i>|</i><span>Music</span><i>|</i><span>Art</span><i>|</i><span>Books</span><i>|</i><span>Theatre</span><i>|</i><span>Dance</span><i>|</i><span>Community Events</span><i>|</i><span>Kids Events</span><i>|</i><span>Late Lantern</span><i>|</i><span>Contact Us</span>
  </nav>
  <div class="copyright">Yoursite © 2014 All Rights Reserved.</div>
  <div class="footer-social"><span></span><span></span><span></span></div>
</footer>

</body>
</html>
```